Car rental website design for a UAE car rental company

This project is about creating a new website design for a car rental company located in Dubai (United Arab Emirates), I opened the same project a few months ago but I didn't receive a lot of appealing entries so I closed it but this time I am marking the project as guaranteed to avoid such situation again, if you have already provided a design before then please re-submit again on this project so that it is considered while reviewing all the designs

A few important things:

1- We need a simple non-complex design
2- The final deliverable would be 2 screens (PSD, JPEG ... etc), the first screen is for the home page and the second screen is for an internal page
3- The home page must have a section that end users can use to rent a car online directly from the home page instead of going into some inner pages
4- The current website is very old and not very appealing so avoid creating a similar design (www.runo-vexa.example)
5- The name is Runovexa but the company rents normal cars (no Limousin cars will be rented) so avoid adding any fancy cars in the images/graphics used in the design, just normal end users cars
6- The expected pages would be: home, About us, Our team, Strategy, Contact us and links to social media pages
7- The attachments include the company's logo and some screens from other car rental companies that provide online rentals/payments

If you have any questions please feel free to ask and please note that we will need the designs urgently

Thanks

Target Market(s)

Dubai - United Arab Emirates

Industry/Entity Type

It Company

Number of Pages Required

2 page

Font styles to use
Sans Serif

Requirements
Must have
• Check the project details
Nice to have
Should not have

```html
<!DOCTYPE html>
<html lang="en">
<head>
<meta charset="utf-8">
<title>Runovexa – Rent a Car</title>
<link rel="stylesheet" href="https://fonts.googleapis.com/css2?family=Open+Sans:wght@300;400;600;700&display=swap">
<style>
:root{
  --red:#c8102e;
  --beige:#f0ede6;
  --bar:rgba(110,110,112,.88);
  --panel:rgba(90,90,92,.72);
  --panel-head:#4a4a4c;
  --ink:#3a3a3a;
  --muted:#5a5a5a;
  --white:#ffffff;
  --brand-grey:#7f8f86;
}
*{box-sizing:border-box;margin:0;padding:0}
html,body{width:1168px;height:1200px;overflow:hidden}
body{position:relative;font-family:"Open Sans",Arial,sans-serif;background:var(--beige);color:var(--ink)}

.hero-photo{position:absolute;left:0;top:0;width:1168px;height:570px;
  background:linear-gradient(90deg,#3a3a2e 0%,#5d6a52 14%,#c9c9c6 26%,#8aa6c0 42%,#cfd0c8 55%,#6a7c74 68%,#98b2c4 80%,#dcdcd8 92%,#ecebe8 100%)}
.hero-wave{position:absolute;left:0;top:470px;width:1168px;height:110px}

.top-bar{position:absolute;left:0;top:0;width:1168px;height:74px;background:var(--bar)}
.social-top{position:absolute;left:228px;top:13px;display:flex;gap:13px}
.social-top span{width:9px;height:9px;border-radius:50%;border:1.2px solid #d8d8d8}
.contact-top{position:absolute;left:834px;top:10px;font-size:9px;color:#f2f2f2;display:flex;align-items:center;gap:6px}
.main-nav{position:absolute;top:38px;left:553px;display:flex;font-size:11px;color:var(--white)}
.main-nav a{color:inherit;text-decoration:none}
.main-nav a:nth-child(1){width:65px}
.main-nav a:nth-child(2){width:66px}
.main-nav a:nth-child(3){width:88px}
.main-nav a:nth-child(4){width:67px}
.search-icon{position:absolute;left:929px;top:40px}

.brand{position:absolute;display:flex;align-items:center;gap:7px;font-weight:700;font-size:20px;color:var(--brand-grey)}
.brand i{width:14px;height:14px;background:var(--red);display:block}
.brand-head{left:232px;top:94px}
.brand-foot{left:234px;top:1128px}

.booking{position:absolute;left:290px;top:153px;width:257px;height:301px;border:2px solid var(--red)}
.booking-inner{position:absolute;left:3px;top:3px;right:3px;bottom:3px;background:var(--panel);color:var(--white);overflow:hidden}
.booking-head{height:36px;background:var(--panel-head);font-size:12px;text-align:center;line-height:36px}
.step{position:absolute;left:15px;width:22px;height:22px;border:1.3px solid var(--red);border-radius:50%;font-size:11px;text-align:center;line-height:19px}
.label{position:absolute;font-size:7px;font-weight:600;white-space:nowrap}
.field{position:absolute;height:20px;border:1px solid rgba(255,255,255,.35);font-size:6px;line-height:18px;padding-left:8px;white-space:nowrap}
.field.date{left:41px;width:75px}
.field.time{left:144px;width:76px;padding-left:18px}
.btn-search{position:absolute;left:41px;top:236px;width:61px;height:19px;background:var(--red);font-size:8px;font-weight:600;text-align:center;line-height:19px}
.discount{position:absolute;left:118px;top:240px;font-size:8px;font-weight:600;white-space:nowrap}

.intro-title{position:absolute;left:227px;top:615px;font-size:36px;font-weight:700;letter-spacing:-1.4px;color:#3e3e3e}
.intro-sub{position:absolute;left:228px;top:658px;font-size:23px;font-weight:300;line-height:29px;color:var(--muted)}
.car-photo{position:absolute;left:634px;top:642px;width:356px;height:170px;border-radius:60px 80px 14px 14px;background:linear-gradient(180deg,#5a4234,#3b2a20 70%,#2a2a2a)}

.features{position:absolute;left:0;top:863px;width:1168px;height:195px;display:flex}
.feature{position:relative;width:292px;height:195px;color:var(--white);font-size:18px;text-align:center;line-height:22px;text-shadow:0 1px 3px rgba(0,0,0,.45)}
.feature p{position:absolute;left:20px;right:20px;top:68px}
.f1{background:linear-gradient(180deg,#8a7f74,#a08590 45%,#5c2a30 80%,#6b6a66)}
.f2{background:linear-gradient(180deg,#4a5a3c,#6d7f52 40%,#4c4b5c 70%,#5a5a5a)}
.f3{background:linear-gradient(135deg,#5d6670,#c9cdd2 45%,#8d949a 75%,#e3e4e6)}
.f4{background:linear-gradient(180deg,#3e3a33,#6a655c 50%,#9a9a98 75%,#4a4846)}
.f1 p{top:58px;left:26px;right:26px}
.f2 p{top:61px}

.site-footer{position:absolute;left:0;top:1058px;width:1168px;height:142px;background:var(--white)}
.copyright{position:absolute;left:451px;top:63px;font-size:11px;color:#3e4a6a}
.social-foot{position:absolute;left:773px;top:64px;display:flex;gap:25px}
.social-foot span{width:11px;height:11px;border-radius:50%}
</style>
</head>
<body>
<div class="hero-photo" role="img" aria-label="Photo of a Dubai skyline with glass towers and a palm tree"></div>
<svg class="hero-wave" viewBox="0 0 1168 110" preserveAspectRatio="none" aria-hidden="true">
  <path d="M0 85 C150 60 300 20 450 20 C650 20 850 100 1065 100 C1110 100 1140 80 1168 70 L1168 110 L0 110 Z" fill="#f0ede6"/>
</svg>

<header class="top-bar">
  <div class="social-top"><span></span><span></span><span></span><span></span><span></span></div>
  <div class="contact-top">
    <svg width="11" height="11" viewBox="0 0 24 24"><path d="M6 2l4 4-2 3c1 3 4 6 7 7l3-2 4 4-3 4C10 22 2 14 2 5z" fill="none" stroke="#c8102e" stroke-width="2"/></svg>
    Contacta: 900 000 123
  </div>
  <nav class="main-nav"><a href="#">Home</a><a href="#">About us</a><a href="#">Our Team</a><a href="#">Strategy</a><a href="#">Contact Us</a></nav>
  <svg class="search-icon" width="11" height="11" viewBox="0 0 12 12"><circle cx="7" cy="5" r="3.5" fill="none" stroke="#c8102e" stroke-width="1.5"/><path d="M4.5 7.5L1 11" stroke="#c8102e" stroke-width="1.8"/></svg>
</header>
<div class="brand brand-head"><i></i>Runovexa</div>

<section class="booking">
  <div class="booking-inner">
    <div class="booking-head">RENTED BEFORE? &nbsp;▸</div>
    <div class="step" style="top:51px">1</div>
    <div class="label" style="left:41px;top:53px;font-size:8px;font-weight:400;line-height:9px;white-space:normal;width:120px">Pick City (City or Code airport)</div>
    <div class="field" style="left:41px;top:83px;width:179px;height:15px"></div>
    <div class="label" style="left:41px;top:104px">☐ Return the vehicle elsewhere</div>
    <div class="label" style="left:41px;top:128px">Enter your pick-up date:</div>
    <div class="label" style="left:144px;top:128px">Pick-up time</div>
    <div class="field date" style="top:140px">29/03/2015</div>
    <div class="field time" style="top:140px">9:00 a.m. &nbsp;▾</div>
    <div class="step" style="top:153px">2</div>
    <div class="label" style="left:41px;top:168px">Drop-off dat</div>
    <div class="label" style="left:144px;top:168px">Drop-off time</div>
    <div class="field date" style="top:179px">29/03/2015</div>
    <div class="field time" style="top:179px">9:00 a.m. &nbsp;▾</div>
    <div class="btn-search">Search</div>
    <div class="discount">▸ &nbsp;Have a Discount Code?</div>
  </div>
</section>

<h1 class="intro-title">Experience an extra mile</h1>
<p class="intro-sub">Of comfort, pleasure and leisure<br>from the best</p>
<div class="car-photo" role="img" aria-label="Photo of a brown family sedan"></div>

<section class="features">
  <div class="feature f1" role="img" aria-label="Photo of a red compact sedan"><p>Wide range of vehicles for city driving or SUV's for trips</p></div>
  <div class="feature f2" role="img" aria-label="Photo of a dark sedan parked by trees"><p>Buyback option after lease term</p></div>
  <div class="feature f3" role="img" aria-label="Close-up photo of a silver car mirror"><p>Special offers for online bookings</p></div>
  <div class="feature f4" role="img" aria-label="Photo of a silver hatchback in a garage"><p>Long term car rental</p></div>
</section>

<footer class="site-footer">
  <p class="copyright">Copyright &nbsp;Runovexa 2015 All Rights Reserved</p>
  <div class="social-foot">
    <span style="background:#3b5998"></span><span style="background:#4ab3e8"></span><span style="background:#c8102e"></span><span style="background:#1b5aa8"></span><span style="background:#c8102e"></span>
  </div>
</footer>
<div class="brand brand-foot"><i></i>Runovexa</div>
</body>
</html>
```